Self-Help & Training Association Business Card Design Project

We need double-sided business card for our Self-Help and Training Association called "Crescitalba".

We want Pibo.com to print them, both Velta and Standard Business Card format (**PLEASE DON'T SUBMIT ROUNDED-CORNERS CARDS).

(more info: http://uk.pibo-print.example)

We ask designers to submit project based on our logo (attached) and color-set and to do it according to Pibo.com designing guidelines.

We will print three variations (for three people) of the business card.

Let's apply now!

Thank you!

Target Market(s)

Common people

Industry/Entity Type

Business

Requirements
Must have
• Strings needed:

Association Name: Crescitalba
Tagline: Imparare per stare bene
Web: www.crescitalba.example

Person Name: Luca Ferrandi
Person Title: Direttore Scientifico e Lead Trainer
Mobile: (+39) 347 5081934
E-mail: luca@crescitalba.example

Could be a nice idea to put general details on the front and personal details on the back of the card.

-
Artwork guidelines
You can use PIBO's online tools to position and crop your images, but if you'd like to pre-design your Business Cards, before you upload these are the dimensions you need:

Full bleed size
(Recommended for creating artwork - this includes the bleed, which will be cropped in production. Please note, you do not need to add crop marks to your artwork)

1039 x 697 pixels (300dpi)
88mm x 59mm (300dpi)
3.46" x 2.32" (300dpi)
Final size when trimmed
84mm x 55mm
3.30" x 2.16"
Accepted file types
We accept high resolution GIFs, PNGs, PDFs, and JPGs.

-

See http://www.crescitalba.example/ for colors and style reference.

Thank you!
Nice to have
• If you still have empty space, this quote will be cool to be added:

"Non è il più forte o il più intelligente a sopravvivere, ma chi si adatta più velocemente al cambiamento. (G. Pellow)"

```html
<!DOCTYPE html>
<html lang="it">
<head>
<meta charset="utf-8">
<title>Crescitalba – Biglietto da visita</title>
<link rel="stylesheet" href="https://fonts.googleapis.com/css2?family=Michroma&family=Oswald:wght@500&display=swap">
<style>
  :root {
    --sheet: #ffffff;
    --edge: #2a2f36;
    --card-top: #f2f5f9;
    --card-mid: #b9cadb;
    --card-bottom: #5482ab;
    --ink: #111418;
    --white: #ffffff;
    --mark: #4fb7b8;
    --url-red: #d4161c;
    --url-shadow: #3b4450;
    --text-glow: rgba(30, 50, 75, 0.55);
  }
  * { margin: 0; padding: 0; box-sizing: border-box; }
  html, body {
    width: 917px; height: 1200px; overflow: hidden;
    background: var(--sheet);
  }
  .sheet { position: relative; width: 917px; height: 1200px; }
  .card {
    position: absolute; left: 14px; width: 888px;
    background: linear-gradient(180deg, var(--card-top) 0%, var(--card-mid) 50%, var(--card-bottom) 100%);
    border-left: 3px solid var(--edge);
    overflow: hidden;
  }
  .card--front { top: 0; height: 597px; }
  .card--back { top: 600px; height: 600px; }
  .brand-dot {
    position: absolute; border-radius: 50%;
    background: var(--mark);
  }
  .brand-name {
    position: absolute; font-family: "Michroma", sans-serif; font-weight: 400;
    color: var(--ink); white-space: nowrap; letter-spacing: 1px;
  }
  .tagline {
    position: absolute; font-family: "Michroma", sans-serif;
    color: var(--white); white-space: nowrap; text-transform: uppercase;
    text-shadow: 1px 1px 0 #3d4650, -1px -1px 0 #3d4650, 1px -1px 0 #3d4650, -1px 1px 0 #3d4650, 3px 4px 5px rgba(0,0,0,0.45);
  }
  .tagline em { font-style: italic; }
  .site-url {
    position: absolute; font-family: "Oswald", sans-serif; font-weight: 500;
    white-space: nowrap; text-transform: uppercase; transform-origin: left top;
  }
  .site-url--main {
    color: var(--url-red); -webkit-text-stroke: 1px #7a0a0e;
    left: 138px; top: 292px; font-size: 58px; transform: scaleX(0.86);
  }
  .site-url--echo {
    color: var(--url-shadow); filter: blur(3px); opacity: 0.85;
    left: 200px; top: 402px; font-size: 58px; transform: scaleX(0.84);
  }
  .quote {
    position: absolute; left: 30px; top: 543px; width: 700px;
    font-family: "Michroma", sans-serif; font-size: 12.4px; line-height: 20px;
    color: var(--white); text-transform: uppercase;
    text-shadow: 0 0 3px var(--text-glow);
  }
  .next-arrow { position: absolute; left: 745px; top: 517px; }
  .person {
    position: absolute; left: 24px; font-family: "Michroma", sans-serif;
    color: var(--white); text-transform: uppercase; white-space: nowrap;
    text-shadow: 0 0 6px var(--text-glow);
  }
  .person__name { top: 304px; font-size: 31px; }
  .person__role { top: 348px; font-size: 25px; }
  .person__phone { top: 423px; font-size: 23px; }
  .person__mail { top: 457px; font-size: 23px; }
</style>
</head>
<body>
<main class="sheet">
  <section class="card card--front" aria-label="Fronte">
    <span class="brand-dot" style="left:20px; top:10px; width:150px; height:150px;"></span>
    <h1 class="brand-name" style="left:230px; top:64px; font-size:48px;">CRESCITALBA</h1>
    <p class="tagline" style="right:18px; top:164px; font-size:25px;">Imparare per stare <em>bene</em></p>
    <p class="site-url site-url--main">www.crescitalba.example</p>
    <p class="site-url site-url--echo" aria-hidden="true">www.crescitalba.example</p>
    <p class="quote">"Non è il più forte o il più intelligente a sopravvivere, ma chi si adatta più velocemente al cambiamento. (G. Pellow)"</p>
    <svg class="next-arrow" width="140" height="66" viewBox="0 0 140 66" aria-hidden="true">
      <path d="M0 2 H62 V20 H24 V36 H84 V24 L138 46 L84 64 V52 H0 Z" fill="#ffffff" stroke="#8fa6bb" stroke-width="1"/>
    </svg>
  </section>

  <section class="card card--back" aria-label="Retro">
    <span class="brand-dot" style="left:20px; top:14px; width:215px; height:215px;"></span>
    <h2 class="brand-name" style="left:305px; top:96px; font-size:42px; transform:rotate(-3deg); transform-origin:left bottom;">CRESCITALBA</h2>
    <p class="tagline" style="left:318px; top:212px; font-size:24px; transform:rotate(-5.5deg); transform-origin:left bottom;">Imparare per stare <em>bene</em></p>
    <p class="person person__name">Luca Ferrandi</p>
    <p class="person person__role">Direttore Scientifico e Lead Trainer</p>
    <p class="person person__phone">Mobile: (+39) 347 5081934</p>
    <p class="person person__mail">E-mail: luca@crescitalba.example</p>
  </section>
</main>
</body>
</html>
```